Parades of Glint stationary design

Parades of Glint (www.paradesofglint.example) is a company that operates events that display the worlds most exotic cars, motorcyles, aircraft, watercraft and luxury brands. we are cutting edge and are looking for a clean , modern stationary design. our sponsors of the events include names like Vantorro, Molvecci, Castelvandri, Kelmayr, Ravelli, Lun vorel, Quastmere and many other big names. we currently operate in florida but are looking to get into new York and California. I added the logo and two car images.car images are optional and not mandatory for the design. Just thought we would add to see what happens.

Target Market(s)

high end , clean design think KELMAYR DESGN style sharp, clean, cutting edge must appeal to the high end luxury brand corporate companies and car, motorcycle, boat, aircraft and luxury brand collectors

Industry/Entity Type

Events

Font styles to use
Sans Serif

Requirements
Must have
• our contact information
• Neil Horvath
• President
• 352-555-0174
• www.paradesofglint.example
• PO Box 4862
• Dunmore, FL 32000
• for business card my email is neil@paradesofglint.example

```html
<!DOCTYPE html>
<html lang="en">
<head>
<meta charset="utf-8">
<title>Parades of Glint — Stationery</title>
<link rel="stylesheet" href="https://fonts.googleapis.com/css2?family=Open+Sans:wght@400;600;700&display=swap">
<style>
  :root {
    --bg: #efefef;
    --paper: #ffffff;
    --edge: #e2e2e2;
    --red: #c4121a;
    --slate: #8e9a9a;
    --ink: #3a3a3a;
    --muted: #6b6b6b;
  }
  * { box-sizing: border-box; margin: 0; padding: 0; }
  html, body { width: 1200px; height: 937px; overflow: hidden; background: var(--bg); }
  body { position: relative; font-family: "Open Sans", Arial, sans-serif; color: var(--ink); }

  .sheet { position: absolute; background: var(--paper); border: 1px solid var(--edge); }

  .brand { position: absolute; display: flex; align-items: center; gap: 6px; }
  .brand-mark { background: var(--red); flex: none; }
  .brand-name { color: var(--slate); font-weight: 600; white-space: nowrap; letter-spacing: 0.5px; }

  .contact { position: absolute; display: flex; flex-direction: column; align-items: flex-end; }
  .contact-row { display: flex; align-items: center; gap: 4px; text-align: right; color: var(--muted); line-height: 1.25; }
  .contact-icon { flex: none; display: block; }

  /* letterhead */
  .letterhead { left: 185px; top: 66px; width: 385px; height: 546px; }
  .letterhead .brand { left: 40px; top: 66px; }
  .letterhead .brand-mark { width: 9px; height: 9px; }
  .letterhead .brand-name { font-size: 16px; }
  .letterhead .contact { right: 18px; top: 26px; gap: 9px; }
  .letterhead .contact-row { font-size: 4px; }
  .letter { position: absolute; left: 36px; top: 138px; width: 300px; font-size: 5.2px; line-height: 1.55; color: #555; }
  .letter p { margin-bottom: 7px; }
  .letter .date { margin-bottom: 10px; }
  .letter .greet strong { color: var(--ink); }
  .letter .gap { margin-bottom: 16px; }
  .signature { width: 34px; height: 16px; margin: 2px 0 6px; background: linear-gradient(90deg, #ededed, #d9d9d9); }
  .signer { font-weight: 700; color: var(--ink); }

  /* folder cover */
  .folder { left: 636px; top: 41px; width: 458px; height: 575px; }
  .folder .brand { left: 84px; top: 296px; gap: 12px; }
  .folder .brand-mark { width: 18px; height: 18px; }
  .folder .brand-name { font-size: 36px; }

  /* business cards */
  .card { border-radius: 7px; width: 177px; height: 100px; }
  .card-front { left: 45px; top: 658px; }
  .card-back { left: 45px; top: 785px; }
  .card .holder { position: absolute; left: 8px; top: 45px; font-size: 5px; color: var(--muted); }
  .card .holder b { color: var(--ink); text-transform: uppercase; }
  .card-front .contact { right: 9px; top: 22px; gap: 6px; }
  .card-front .contact-row { font-size: 3.4px; }
  .card-back .brand { left: 34px; top: 42px; }
  .card-back .brand-mark { width: 7px; height: 7px; }
  .card-back .brand-name { font-size: 13px; }

  /* envelopes */
  .envelope { width: 431px; height: 208px; }
  .envelope-front { left: 265px; top: 672px; }
  .envelope-front .brand { left: 22px; top: 30px; }
  .envelope-front .brand-mark { width: 8px; height: 8px; }
  .envelope-front .brand-name { font-size: 14px; }
  .envelope-back { left: 737px; top: 672px; overflow: hidden; }
  .flap { position: absolute; left: 0; top: 0; width: 100%; height: 72px; background: var(--red); border-radius: 0 0 26px 26px; display: flex; align-items: center; justify-content: center; color: #fff; font-size: 15px; letter-spacing: 2px; }
  .flap b { font-weight: 600; letter-spacing: 1px; }
</style>
</head>
<body>

<svg width="0" height="0" style="position:absolute" aria-hidden="true">
  <defs>
    <symbol id="icon-phone" viewBox="0 0 10 10"><rect width="10" height="10" rx="1.5" fill="#c4121a"/><path d="M3 2.5c.4 2.3 1.9 3.9 4.5 4.6l.6-1.1-1.3-.7-.6.6C5.3 5.4 4.6 4.7 4.2 3.8l.6-.6-.7-1.3z" fill="#fff"/></symbol>
    <symbol id="icon-web" viewBox="0 0 10 10"><rect width="10" height="10" rx="1.5" fill="#c4121a"/><circle cx="5" cy="5" r="2.8" fill="none" stroke="#fff" stroke-width=".7"/><path d="M2.2 5h5.6M5 2.2v5.6" stroke="#fff" stroke-width=".6"/></symbol>
    <symbol id="icon-mail" viewBox="0 0 10 10"><rect width="10" height="10" rx="1.5" fill="#c4121a"/><rect x="2.2" y="3.2" width="5.6" height="3.8" fill="none" stroke="#fff" stroke-width=".7"/><path d="M2.2 3.2 5 5.3l2.8-2.1" fill="none" stroke="#fff" stroke-width=".7"/></symbol>
    <symbol id="icon-pin" viewBox="0 0 10 10"><rect width="10" height="10" rx="1.5" fill="#c4121a"/><path d="M5 8.2S2.8 5.7 2.8 4.2a2.2 2.2 0 0 1 4.4 0C7.2 5.7 5 8.2 5 8.2z" fill="#fff"/><circle cx="5" cy="4.2" r=".8" fill="#c4121a"/></symbol>
  </defs>
</svg>

<!-- Letterhead -->
<section class="sheet letterhead">
  <div class="brand"><span class="brand-mark"></span><span class="brand-name">Parades of Glint</span></div>
  <div class="contact">
    <div class="contact-row"><span>352-555-0174<br>352-555-0174</span><svg class="contact-icon" width="9" height="9"><use href="#icon-phone"/></svg></div>
    <div class="contact-row"><span>www.paradesofglint.example</span><svg class="contact-icon" width="9" height="9"><use href="#icon-web"/></svg></div>
    <div class="contact-row"><span>neil@paradesofglint.example</span><svg class="contact-icon" width="9" height="9"><use href="#icon-mail"/></svg></div>
    <div class="contact-row"><span>PO Box 4862<br>Dunmore, FL 32000</span><svg class="contact-icon" width="9" height="9"><use href="#icon-pin"/></svg></div>
  </div>
  <div class="letter">
    <p class="date">July 2, 2012</p>
    <p class="greet"><strong>Dear Cli,</strong><br>ABC Building, def St., Country Name</p>
    <p class="gap">is simply dummy text of the printing and typesetting industry. Lorem Ipsum has been the industry's standard dummy text ever since the 1500s, when an unknown printer took a galley of type and scrambled it to make a type specimen book. It has survived not only five centuries, but also the leap into electronic typesetting, remaining essentially unchanged. It was popularised in the 1960s with the release of Transfix sheets containing Lorem Ipsum passages, and more recently with desktop publishing software like Quillset Pagewright including versions of Lorem Ipsum.</p>
    <p class="gap">is simply dummy text of the printing and typesetting industry. Lorem Ipsum has been the industry's standard dummy text ever since the 1500s, when an unknown printer took a galley of type and scrambled it to make</p>
    <p>is simply dummy text of the printing and typesetting industry. Lorem Ipsum has been the industry's standard dummy text ever since the 1500s, when an unknown printer took a galley of type and scrambled it to make a type specimen book. It has survived not only five centuries, but also the leap into electronic typesetting, remaining essentially unchanged. It was popularised in the 1960s with the release of Transfix sheets containing Lorem Ipsum passages, and more recently with desktop publishing software like Quillset Pagewright including versions of Lorem Ipsum.</p>
    <p>Best Regards,</p>
    <div class="signature" role="img" aria-label="Handwritten signature"></div>
    <p><span class="signer">Neil Horvath</span><br>President<br>ABC Building, def St., Country Name</p>
  </div>
</section>

<!-- Folder cover -->
<section class="sheet folder">
  <div class="brand"><span class="brand-mark"></span><span class="brand-name">Parades of Glint</span></div>
</section>

<!-- Business card front -->
<section class="sheet card card-front">
  <p class="holder"><b>Neil</b> Horvath<br>President</p>
  <div class="contact">
    <div class="contact-row"><svg class="contact-icon" width="7" height="7"><use href="#icon-phone"/></svg><span>352-555-0174</span></div>
    <div class="contact-row"><span>www.paradesofglint.example</span><svg class="contact-icon" width="7" height="7"><use href="#icon-web"/></svg></div>
    <div class="contact-row"><svg class="contact-icon" width="7" height="7"><use href="#icon-mail"/></svg><span>neil@paradesofglint.example</span></div>
    <div class="contact-row"><span>PO Box 4862<br>Dunmore, FL 32000</span><svg class="contact-icon" width="7" height="7"><use href="#icon-pin"/></svg></div>
  </div>
</section>

<!-- Business card back -->
<section class="sheet card card-back">
  <div class="brand"><span class="brand-mark"></span><span class="brand-name">Parades of Glint</span></div>
</section>

<!-- Envelope front -->
<section class="sheet envelope envelope-front">
  <div class="brand"><span class="brand-mark"></span><span class="brand-name">Parades of Glint</span></div>
</section>

<!-- Envelope back -->
<section class="sheet envelope envelope-back">
  <div class="flap">www.<b>paradesofglint</b>.example</div>
</section>

</body>
</html>
```